Concise,Good colour matching,Good looks design for "HERD SURE QUICK ASSAY FOR LIVESTOCK"

Product Positioning: Affordable test for Large Animals (Livestock/Veterinary Use)
Product Name: HERD SURE Quick Assay Kit (for large animals, e.g., cattle, horses, swine,Avian,sheep).

2. Packaging Requirements

A. Visual Design
Color Scheme:
Green/Blue/Orange/Yellow/Red/Gray/White(chose 2~4 colors)

Mandatory Info:
Brand logo ("HERD SURE")

Target Market(s)

Southeast Asia, Africa, Middle East, South America

Industry/Entity Type

Veterinary diagnostic for LIVESTOCK

Colors

Designer to choose colors to be used in the design.

Requirements
Nice to have
• Concise,Good colour matching,Good looks

```html
<!DOCTYPE html>
<html lang="en">
<head>
<meta charset="utf-8">
<title>HERD SURE Quick Assay Kit – Box Dieline</title>
<link href="https://fonts.googleapis.com/css2?family=Montserrat:wght@500;700;800&display=swap" rel="stylesheet">
<style>
  :root{
    --green:#0b6412;
    --orange:#f59a00;
    --orange-deep:#f07c00;
    --yellow:#ffc400;
    --white:#ffffff;
    --cut:#555555;
    --ink:#111111;
  }
  *{margin:0;padding:0;box-sizing:border-box}
  html,body{width:1200px;height:675px;overflow:hidden;background:var(--white)}
  body{font-family:"Montserrat",Arial,sans-serif}
  .canvas{position:relative;width:1200px;height:675px}
  .dieline{position:absolute;left:0;top:0}
  .t{position:absolute;line-height:1.15;white-space:nowrap}
  .size-note{left:1044px;top:42px;font-size:15px;font-weight:500;color:var(--ink)}
  .brand{font-weight:800;letter-spacing:0.5px}
  .flip{transform:rotate(180deg)}
  .top-brand{left:108px;top:98px;width:114px;font-size:17px;color:var(--orange);text-align:right}
  .top-tagline{left:244px;top:127px;width:136px;font-size:10.5px;font-weight:700;color:var(--white);text-align:left}
  .front-brand{left:197px;top:364px;font-size:26px;color:var(--white)}
  .front-info{left:168px;top:396px;width:210px;font-size:8.4px;font-weight:700;color:var(--white);text-align:center}
  .side-label{left:407px;top:445px;width:99px;height:16px;background:var(--orange);color:var(--white);font-size:9px;font-weight:800;padding:3px 5px}
  .side-info{left:506px;top:444px;width:104px;font-size:4.6px;font-weight:500;color:var(--ink);text-align:center}
  .side-info b{font-weight:700}
  .back-brand{left:740px;top:364px;font-size:25px;color:var(--white)}
  .back-tagline{left:742px;top:395px;width:148px;font-size:11px;font-weight:700;color:var(--white);text-align:center}
  .features{left:948px;top:336px;width:196px;color:var(--white);white-space:normal}
  .features .head{display:flex;align-items:baseline;gap:10px;margin-bottom:8px;white-space:nowrap}
  .features .kicker{font-size:10px;font-weight:800;color:var(--orange)}
  .features .head .brand{font-size:17px;color:var(--white)}
  .features p{font-size:7.8px;font-weight:500;line-height:1.3;margin-bottom:8px}
  .features p b{font-weight:700}
  .bottom-brand{left:86px;top:517px;width:308px;font-size:18px;color:var(--green);text-align:center}
  .bottom-tagline{left:86px;top:540px;width:308px;font-size:11.5px;font-weight:700;color:var(--green);text-align:center}
</style>
</head>
<body>
<main class="canvas">
  <svg class="dieline" width="1200" height="675" viewBox="0 0 1200 675" xmlns="http://www.w3.org/2000/svg">
    <rect class="band-top" x="86" y="123" width="308" height="36" fill="var(--green)"/>
    <g class="photo-grid" role="img" aria-label="Grid of six livestock photographs tinted orange: cattle, sheep, pig, goat, chicken and horse">
      <rect x="86" y="159" width="103" height="77" fill="#f6a000"/>
      <rect x="189" y="159" width="102" height="77" fill="#f08a00"/>
      <rect x="291" y="159" width="103" height="77" fill="#f7a81a"/>
      <rect x="86" y="236" width="103" height="77" fill="#f58a00"/>
      <rect x="189" y="236" width="102" height="77" fill="#fbb400"/>
      <rect x="291" y="236" width="103" height="77" fill="#f59c10"/>
    </g>
    <rect class="panel-front" x="86" y="313" width="308" height="165" fill="var(--green)"/>
    <rect class="panel-back" x="620" y="313" width="534" height="165" fill="var(--green)"/>
    <rect class="brand-square" x="150" y="358" width="40" height="40" fill="var(--orange)"/>
    <rect class="brand-square" x="690" y="358" width="40" height="40" fill="var(--orange)"/>

    <g fill="none" stroke="var(--cut)" stroke-width="0.6">
      <path d="M86 87 V60 Q86 46 100 46 H380 Q394 46 394 60 V87"/>
      <path d="M86 87 H394 M86 87 V478 M394 87 V478"/>
      <path d="M86 313 L44 319 V472 L86 478"/>
      <path d="M394 313 L400 307 V210 H585 Q607 210 608 232 L612 300 L620 306 V313"/>
      <path d="M928 313 V306 L932 303 L936 232 Q938 210 960 210 H1148 V306 L1154 313"/>
      <path d="M394 313 H620 M394 478 H620 M620 313 V478 M1154 313 V478"/>
      <path d="M394 478 L507 548 V576 Q507 590 521 590 H620 V478"/>
      <path d="M620 478 L692 590 V618 Q692 631 705 631 H843 Q856 631 856 618 V590 L928 478"/>
      <path d="M928 478 V590 H1029 Q1041 590 1041 578 V548 L1154 478"/>
      <path d="M86 478 V631 H145 Q158 631 158 618 V590 H322 V618 Q322 631 335 631 H394 V478"/>
    </g>
  </svg>

  <div class="t size-note">150×110×80mm</div>

  <div class="t brand top-brand flip">HERD SURE</div>
  <div class="t top-tagline flip">Affordable Diagnostics<br>for Healthy Herds</div>

  <div class="t brand front-brand">HERD SURE</div>
  <div class="t front-info">Storage: 2-30 °C,Do not freeze<br>See the instructions for other contents</div>

  <div class="t brand side-label">HERD SURE</div>
  <div class="t side-info"><b>Manufactured by VELMORIN</b><br>Storage: 2-30 °C,Do not freeze<br>See the instructions for other contents</div>

  <div class="t brand back-brand">HERD SURE</div>
  <div class="t back-tagline">Affordable Diagnostics<br>for Healthy Herds</div>

  <section class="t features">
    <div class="head"><span class="kicker">QUICK ASSAY</span><span class="brand">HERD SURE</span></div>
    <p><b>Fast &amp; Efficient:</b> Rapid test results in less than 10 minutes from prep to completion</p>
    <p><b>Affordable:</b> Colloidal gold-based rapid tests that combine high accuracy with cost-effectiveness</p>
    <p><b>Reliable &amp; Simple:</b>Stable test performance with 2-30 °C, Easy to operate,no professional skills required.</p>
  </section>

  <div class="t brand bottom-brand">HERD SURE</div>
  <div class="t bottom-tagline">Affordable Diagnostics<br>for Healthy Herds</div>
</main>
</body>
</html>
```